Web design for software company

I'm a software developer that designs high end specialist web applications, mobile apps and user friendly applications for medium to large customers. I integrate different systems together within a company and provide web based applications or mobile apps to view and edit information in that web of linked systems.

I currently work alone, basically selling my time on specialist projects, but also build my own software solutions which I eventually want to put into the market.

My company name is Overthread (lowercase 'L' for logic) and I work from the Netherlands. I've attached my current logo which is basically just text in VOXbox font. Current colours are mustard yellow and grey, but i'm open to other options to better fit the web design.

I've got a sort of slogan: "Specialized software development" - better ideas are welcome. The slogan in the logo attachment is older.

I'm looking for a site design that reflects my work as being on the cutting edge of technology, but being clear and simple. My thinking with the name Overthread is that it refers to the underlying mechanism and logic of software.

The site will not be text heavy, so some kind of large graphic to do with software design is welcome. I expect about 4 or 5 main pages or sections of the site in which i'll eventually add things like a blog or contact info etc.

Industry/Entity Type

It Company

Number of Pages Required

1 page

Font styles to use
Sans Serif

Requirements
Nice to have
• A large graphic or photo relevant to my focus as a software developer. Something that shows connecting of software systems with perhaps a variety of devices/browsers that would display data from that cloud of systems.
• Something like these (allthough these are ugly - but the idea is what i mean):
• http://img4.pixvaultimages.example/2000517/22458/i/450/pixvault_224581133-Cloud-computing-user-interface.jpg
• http://business.tamblinet.example/images/modules/mobile-device-policy-design-banner.png
• https://www.pagecraftly.example/images/responsive-web-design.jpg
• http://www.norvexa.example/images/web_apps.png
• https://www.keyportal.example/assets/img/product/web-app@2x.png?v2
Should not have
• Photographs of smiling happy people looking at a screen that make it look like it's a huge business with many offices. I'm a one-man company which could perhaps grow a little bit, but i want to focus on my expertise instead of size.

```html
<!DOCTYPE html>
<html lang="en">
<head>
<meta charset="utf-8">
<title>Overthread — Specialized Software Development</title>
<link href="https://fonts.googleapis.com/css2?family=Audiowide&family=Open+Sans:wght@400;600;700&display=swap" rel="stylesheet">
<style>
:root{
  --blue:#1aa3e8;
  --blue-deep:#0d8bd3;
  --dark:#2a2a2a;
  --darker:#1d1d1d;
  --ink:#222;
  --white:#fff;
}
*{box-sizing:border-box;margin:0;padding:0}
html,body{width:1200px;height:3734px;overflow:hidden;background:var(--white)}
body{position:relative;font-family:"Open Sans",Arial,sans-serif;color:var(--ink)}
.abs{position:absolute}
.display{font-family:"Audiowide",Arial,sans-serif;font-weight:400}

/* header */
.topbar{left:0;top:0;width:1200px;height:112px;background:var(--blue)}
.logo-panel{left:0;top:0;width:460px;height:112px}
.brand{left:60px;top:24px;display:flex;align-items:center;gap:14px;font-weight:600;font-size:42px;color:var(--ink)}
.brand-dot{width:50px;height:50px;border-radius:50%;background:var(--blue)}
.contact{top:18px;display:flex;gap:14px;color:var(--white)}
.contact svg{flex:none}
.contact b{display:block;font-size:17px}
.contact span{display:block;font-size:11px;line-height:1.45;font-weight:600}
.socials-top{z-index:3;left:935px;top:94px;width:230px;height:38px;background:var(--white);display:flex;align-items:center;justify-content:center;gap:9px}
.socials-top i{width:24px;height:24px;border-radius:50%;background:var(--darker);display:block}
.nav{z-index:2;left:0;top:112px;width:1200px;height:63px;background:var(--dark)}
.nav a{position:absolute;top:22px;color:var(--white);font-size:13px;font-weight:600;text-decoration:none;letter-spacing:.3px}
.nav a.active::after{content:"";position:absolute;left:-8px;right:-8px;top:36px;height:4px;background:var(--blue)}

/* hero */
.hero{left:0;top:175px;width:1200px;height:510px;background:
  radial-gradient(ellipse 260px 200px at 900px 230px,rgba(40,30,25,.55),transparent 70%),
  radial-gradient(ellipse 380px 220px at 560px 330px,rgba(170,170,175,.45),transparent 70%),
  linear-gradient(160deg,#5a4a3e 0%,#6e6258 40%,#4a4038 75%,#2f2824 100%)}
.hero h1{position:absolute;left:0;width:1200px;top:130px;text-align:center;color:var(--white);font-size:48px;line-height:58px}
.btn{position:absolute;height:38px;border-radius:19px;background:var(--blue);color:var(--white);font-size:12px;font-weight:700;display:flex;align-items:center;justify-content:center;letter-spacing:.3px}
.hero-arrow{position:absolute;top:180px}

/* features */
.features{left:92px;top:588px;width:1012px;height:366px}
.feature{position:absolute;top:0;width:253px;text-align:center;color:var(--white)}
.feature .ring{width:100px;height:100px;border-radius:50%;background:var(--white);border:3px solid var(--darker);margin:62px auto 0;display:flex;align-items:center;justify-content:center}
.feature h3{margin-top:22px;font-size:15px;color:var(--darker)}
.feature p{margin:6px auto 0;width:210px;font-size:12.5px;line-height:19px;font-weight:600}

/* intro */
.section-title{left:0;width:1200px;text-align:center;font-size:40px;color:var(--ink)}
.intro-text{left:120px;width:960px;top:1075px;text-align:center;font-size:15px;line-height:28px;color:#444}

/* photo tiles: flat tones of the photographs they stand for */
.tile{position:absolute}
.t-desk{background:linear-gradient(135deg,#c9b39a 0%,#8c7560 55%,#4d4036 100%)}
.t-office{background:linear-gradient(135deg,#e9ecef 0%,#b7c2cc 50%,#6f7f8e 100%)}
.t-bright{background:linear-gradient(135deg,#f4f4f2 0%,#d9d6d0 55%,#a6a29c 100%)}
.t-dark{background:linear-gradient(135deg,#5b6670 0%,#343c44 60%,#1f2429 100%)}
.t-screen{background:linear-gradient(135deg,#cfe3f2 0%,#7aa6c8 45%,#3b5166 100%)}
.t-color{background:linear-gradient(135deg,#e6c98d 0%,#c7835a 40%,#5f8fb2 100%)}
.t-skin{background:linear-gradient(135deg,#e7d7c6 0%,#b39a84 50%,#5a4c42 100%)}
.tile.blue{background:var(--blue);display:flex;align-items:center;justify-content:center}

/* news */
.news-text{left:100px;width:1000px;top:1890px;text-align:center;font-size:11.5px;line-height:20px;color:#555}
.filter{position:absolute;top:1962px;height:27px;border:1px solid #ddd;border-radius:3px;font-size:11px;font-weight:600;display:flex;align-items:center;justify-content:center;color:#333}
.filter.on{background:var(--blue);border-color:var(--blue);color:var(--white)}
.news-card{position:absolute;width:197px;height:154px}
.hover-card{z-index:2;left:488px;top:2012px;width:224px;height:244px;background:var(--darker);box-shadow:0 6px 18px rgba(0,0,0,.35)}
.hover-card .pic{position:absolute;left:12px;top:12px;width:200px;height:170px;background:linear-gradient(135deg,#b59a7c,#6a5646 60%,#3a302a)}
.hover-card .share{position:absolute;left:87px;top:64px;width:50px;height:50px;border-radius:50%;background:var(--blue);display:flex;align-items:center;justify-content:center}
.hover-card b{position:absolute;left:20px;top:196px;color:var(--white);font-size:12px}
.hover-card span{position:absolute;left:20px;top:216px;color:#bbb;font-size:11px}

/* apps band */
.apps{left:0;top:2428px;width:1200px;height:453px;background:linear-gradient(120deg,#15a6ec 0%,#0fb5f2 55%,#1b9ee4 100%);overflow:hidden}
.apps h2{position:absolute;left:87px;top:76px;color:var(--white);font-size:38px;line-height:52px}
.apps p{position:absolute;left:87px;top:196px;width:450px;color:var(--white);font-size:14.5px;line-height:25px}
.apps .dl{position:absolute;left:145px;top:344px;color:var(--white);font-size:15px;font-weight:600}
.apps .store{position:absolute;top:338px;width:30px;height:30px;border-radius:50%;background:rgba(255,255,255,.85)}
.apps .devices{position:absolute;left:560px;top:20px;width:620px;height:420px;background:
  radial-gradient(ellipse 190px 120px at 200px 140px,rgba(245,248,252,.85),rgba(245,248,252,0) 75%),
  radial-gradient(ellipse 170px 110px at 450px 120px,rgba(235,242,250,.8),rgba(235,242,250,0) 75%),
  radial-gradient(ellipse 200px 110px at 330px 300px,rgba(250,250,250,.8),rgba(250,250,250,0) 75%),
  radial-gradient(ellipse 300px 200px at 320px 210px,rgba(20,30,45,.55),rgba(20,30,45,0) 80%)}

/* testimonials */
.quote{position:absolute;color:var(--white);font-size:15.5px;line-height:28px;padding:24px 56px}
.quote.blue{z-index:2;left:169px;top:3077px;width:430px;height:140px;background:var(--blue)}
.quote.dark{left:578px;top:3102px;width:428px;height:160px;background:#333;padding-top:34px}
.avatar{position:absolute;width:36px;height:36px;border-radius:50%;background:linear-gradient(135deg,#d8c6b4,#7d6a5c)}
.person b{position:absolute;font-size:15px;font-weight:600}
.person span{position:absolute;font-size:11px;color:#888}
.circle-nav{position:absolute;top:3183px;width:40px;height:40px;border-radius:50%;border:1px solid #ddd;display:flex;align-items:center;justify-content:center}

/* footer */
.footer{left:0;top:3369px;width:1200px;height:334px;background:var(--dark);color:#bbb}
.footer h4{position:absolute;top:40px;color:var(--white);font-size:13px;font-weight:700;letter-spacing:.5px}
.footer .brand{left:92px;top:68px;font-size:32px;color:var(--white);gap:10px}
.footer .brand .brand-dot{width:38px;height:38px}
.footer .about{position:absolute;left:92px;top:127px;width:230px;font-size:11.5px;line-height:20px}
.footer .soc{position:absolute;top:218px;width:26px;height:26px;border-radius:50%;background:#555}
.footer ul{position:absolute;list-style:none;font-size:11.5px}
.touch li{display:flex;gap:10px;align-items:flex-start;margin-bottom:10px;line-height:16px}
.touch li i{flex:none;width:10px;height:10px;margin-top:3px;background:var(--blue);border-radius:50%}
.info li{color:var(--white);font-weight:600;font-size:11px;height:30px}
.info li::before{content:"›";margin-right:8px;color:#999}
.footer .nl{position:absolute;left:871px;top:78px;width:232px;font-size:11.5px;line-height:22px}
.footer .input{position:absolute;left:871px;top:164px;width:232px;height:42px;border:1px solid #555;background:#222;color:#aaa;font-size:12px;padding:12px 16px}
.footer .signup{position:absolute;left:871px;top:221px;width:232px;height:42px;background:var(--blue);color:var(--white);font-size:13px;font-weight:600;display:flex;align-items:center;justify-content:center}
.copyright{left:0;top:3703px;width:1200px;height:31px;background:var(--darker);color:#aaa;font-size:11px;display:flex;align-items:center;justify-content:center}
</style>
</head>
<body>

<header>
  <div class="abs topbar"></div>
  <svg class="abs logo-panel" width="460" height="112" viewBox="0 0 460 112"><polygon points="0,0 405,0 460,56 405,112 0,112" fill="#f2f2f2"/></svg>
  <div class="abs brand"><i class="brand-dot"></i>overthread</div>

  <div class="abs contact" style="left:478px">
    <svg width="32" height="42" viewBox="0 0 32 42"><path d="M16 2C8 2 3 8 3 15c0 10 13 25 13 25s13-15 13-25C29 8 24 2 16 2z" fill="#fff"/><circle cx="16" cy="15" r="5" fill="#1aa3e8"/></svg>
    <div><b>Address</b><span>418 Marlow Lane, Suite 12</span><span>Brenford</span></div>
  </div>
  <div class="abs contact" style="left:705px">
    <svg width="38" height="38" viewBox="0 0 38 38"><circle cx="19" cy="19" r="17" fill="none" stroke="#fff" stroke-width="3"/><path d="M13 11l4 0 2 5-3 2c1 3 3 5 6 6l2-3 5 2 0 4c-8 1-17-8-16-16z" fill="#fff"/></svg>
    <div><b>Call Us</b><span>(555) 014-2290</span></div>
  </div>
  <div class="abs contact" style="left:880px">
    <svg width="38" height="38" viewBox="0 0 38 38"><circle cx="19" cy="19" r="17" fill="none" stroke="#fff" stroke-width="3"/><rect x="10" y="13" width="18" height="12" fill="none" stroke="#fff" stroke-width="2"/><path d="M10 13l9 7 9-7" fill="none" stroke="#fff" stroke-width="2"/></svg>
    <div><b>Email Address</b><span>info@overthread.example</span></div>
  </div>
  <div class="abs socials-top"><i></i><i></i><i></i><i></i><i></i></div>

  <nav class="abs nav">
    <a class="active" style="left:112px">HOME</a>
    <a style="left:207px">OUR STORY</a>
    <a style="left:336px">OUR PEOPLE</a>
    <a style="left:473px">WHAT WE DO</a>
    <a style="left:617px">CONTACT US</a>
  </nav>
</header>

<section class="abs hero" role="img" aria-label="Photo of a wooden desk seen from above with a laptop, notebooks, a camera and a cup of coffee">
  <h1 class="display">specialized software<br>development</h1>
  <div class="btn" style="left:411px;top:275px;width:170px">LEARN MORE</div>
  <div class="btn" style="left:612px;top:275px;width:150px">SIGN IN</div>
  <svg class="hero-arrow" style="left:18px" width="20" height="40" viewBox="0 0 20 40"><path d="M17 3L4 20l13 17" fill="none" stroke="#fff" stroke-width="3"/></svg>
  <svg class="hero-arrow" style="left:1142px" width="20" height="40" viewBox="0 0 20 40"><path d="M3 3l13 17L3 37" fill="none" stroke="#fff" stroke-width="3"/></svg>
</section>

<section class="abs features">
  <svg class="abs" style="left:0;top:0" width="1012" height="366" viewBox="0 0 1012 366">
    <polygon points="0,0 253,20 253,340 0,366" fill="#1aa3e8"/>
    <polygon points="253,20 506,2 506,366 253,340" fill="#2ab0f0"/>
    <polygon points="506,2 759,20 759,340 506,366" fill="#1aa3e8"/>
    <polygon points="759,20 1012,0 1012,366 759,340" fill="#2ab0f0"/>
  </svg>
  <div class="feature" style="left:0">
    <div class="ring"><svg width="54" height="54" viewBox="0 0 54 54" fill="none" stroke="#1aa3e8" stroke-width="3"><circle cx="22" cy="24" r="10"/><circle cx="22" cy="24" r="4"/><circle cx="38" cy="36" r="7"/><path d="M22 9v5M22 34v5M7 24h5M32 24h5M38 26v3M38 43v3"/></svg></div>
    <h3 class="display">software development</h3>
    <p>Lorem ipsum dolor sit amet, consectetur adipiscing elit, sed do eiusmod.</p>
  </div>
  <div class="feature" style="left:253px">
    <div class="ring"><svg width="54" height="54" viewBox="0 0 54 54" fill="none" stroke="#1aa3e8" stroke-width="3"><circle cx="20" cy="18" r="7"/><path d="M8 40c0-8 5-13 12-13s12 5 12 13z"/><circle cx="36" cy="22" r="6"/><path d="M34 30c7 0 12 4 12 11h-10"/></svg></div>
    <h3 class="display">mobile apps</h3>
    <p>Lorem ipsum dolor sit amet, consectetur adipiscing elit, sed do eiusmod.</p>
  </div>
  <div class="feature" style="left:506px">
    <div class="ring"><svg width="54" height="54" viewBox="0 0 54 54" fill="none" stroke="#1aa3e8" stroke-width="3"><circle cx="27" cy="27" r="18"/><ellipse cx="27" cy="27" rx="8" ry="18"/><path d="M9 27h36M12 18h30M12 36h30"/></svg></div>
    <h3 class="display">software counsultions</h3>
    <p>Lorem ipsum dolor sit amet, consectetur adipiscing elit, sed do eiusmod.</p>
  </div>
  <div class="feature" style="left:759px">
    <div class="ring"><svg width="54" height="54" viewBox="0 0 54 54" fill="none" stroke="#1aa3e8" stroke-width="3"><rect x="14" y="6" width="26" height="42" rx="4"/><path d="M22 36l5-14 5 14M24 31h6"/><circle cx="27" cy="43" r="1.5"/></svg></div>
    <h3 class="display">web applications</h3>
    <p>Lorem ipsum dolor sit amet, consectetur adipiscing elit, sed do eiusmod.</p>
  </div>
</section>

<h2 class="abs section-title display" style="top:1012px">custom software and consulting</h2>
<p class="abs intro-text">Lorem ipsum dolor sit amet, consectetur adipisicing elit, sed do eiusmod tempor incididunt ut labore et dolore magna aliqua.<br>Utenim ad minim veniam, quis nostrud exercitation ullamco laboris nisi ut aliquip ex ea commodo consequat.</p>
<div class="btn" style="left:523px;top:1158px;width:172px">MORE FEATURES</div>

<section class="abs" style="left:0;top:0">
  <div class="tile t-desk" style="left:0;top:1260px;width:150px;height:162px" role="img" aria-label="Photo of a person working on a laptop"></div>
  <div class="tile t-bright" style="left:152px;top:1260px;width:166px;height:162px" role="img" aria-label="Photo of a bright desk with a monitor"></div>
  <div class="tile t-skin" style="left:320px;top:1260px;width:165px;height:162px" role="img" aria-label="Photo of hands typing on a keyboard"></div>
  <div class="tile t-office" style="left:487px;top:1260px;width:168px;height:162px" role="img" aria-label="Photo of colleagues talking in an office"></div>
  <div class="tile t-bright" style="left:657px;top:1260px;width:329px;height:162px" role="img" aria-label="Photo of a team meeting at a table"></div>
  <div class="tile t-office" style="left:988px;top:1260px;width:212px;height:326px" role="img" aria-label="Photo of a person working at a computer"></div>
  <div class="tile t-dark" style="left:0;top:1424px;width:318px;height:329px" role="img" aria-label="Photo of a developer at a desktop monitor showing charts"></div>
  <div class="tile t-bright" style="left:320px;top:1424px;width:335px;height:162px" role="img" aria-label="Photo of a person writing at a laptop"></div>
  <div class="tile t-screen" style="left:657px;top:1424px;width:161px;height:162px" role="img" aria-label="Photo of a monitor with sticky notes"></div>
  <div class="tile blue" style="left:822px;top:1424px;width:163px;height:162px">
    <svg width="64" height="30" viewBox="0 0 64 30" fill="none" stroke="#fff" stroke-width="2"><circle cx="15" cy="15" r="12"/><path d="M15 9v12M9 15h12"/><circle cx="49" cy="15" r="12"/><path d="M49 13v8"/><circle cx="49" cy="9" r="1" fill="#fff"/></svg>
  </div>
  <div class="tile t-dark" style="left:320px;top:1588px;width:165px;height:165px" role="img" aria-label="Photo of hands holding a smartphone"></div>
  <div class="tile t-color" style="left:487px;top:1588px;width:331px;height:165px" role="img" aria-label="Photo of a desk covered with design sketches"></div>
  <div class="tile t-skin" style="left:820px;top:1588px;width:165px;height:165px" role="img" aria-label="Photo of a person using a keyboard"></div>
  <div class="tile t-screen" style="left:988px;top:1588px;width:212px;height:165px" role="img" aria-label="Photo of a website on a screen"></div>
</section>

<h2 class="abs section-title display" style="top:1824px">Latest news</h2>
<p class="abs news-text">Lorem ipsum dolor sit amet, consetetur sadipscing elitr, sed diam nonumy eirmod tempor invidunt ut labore et dolore magna aliquyam erat, sed diam voluptua. At vero eos et accusam et justo duo dolores et ea rebum. Stet clita kasd gubergren, no sea takimata sanctus est lorem ipsum dolor sit amet.</p>
<div class="filter on" style="left:441px;width:30px">All</div>
<div class="filter" style="left:484px;width:84px">Illustration</div>
<div class="filter" style="left:578px;width:84px">Print Design</div>
<div class="filter" style="left:670px;width:80px">Web Design</div>

<div class="news-card tile t-bright" style="left:85px;top:2032px" role="img" aria-label="News photo of a person at a laptop"></div>
<div class="news-card tile t-office" style="left:292px;top:2032px" role="img" aria-label="News photo of a keyboard at a desk"></div>
<div class="news-card tile t-screen" style="left:706px;top:2032px" role="img" aria-label="News photo of an office with computers"></div>
<div class="news-card tile t-dark" style="left:913px;top:2032px" role="img" aria-label="News photo of a person at a monitor"></div>
<div class="news-card tile t-office" style="left:85px;top:2199px" role="img" aria-label="News photo of a team around a laptop"></div>
<div class="news-card tile t-dark" style="left:292px;top:2199px" role="img" aria-label="News photo of people working at desks"></div>
<div class="news-card tile t-bright" style="left:499px;top:2199px" role="img" aria-label="News photo of a workspace"></div>
<div class="news-card tile t-skin" style="left:706px;top:2199px" role="img" aria-label="News photo of people using laptops"></div>
<div class="news-card tile t-color" style="left:913px;top:2199px" role="img" aria-label="News photo of a responsive design layout on a desk"></div>
<div class="abs hover-card">
  <div class="pic" role="img" aria-label="News photo of a tablet and photos on a table"></div>
  <div class="share"><svg width="24" height="20" viewBox="0 0 24 20"><path d="M14 2l8 7-8 7v-4c-6 0-10 2-12 6 1-7 5-11 12-12z" fill="#fff"/></svg></div>
  <b>Great Productivity</b><span>Web Design</span>
</div>

<section class="abs apps">
  <h2 class="display">High end web and<br>mobile applications</h2>
  <p>Eleifend morbi orci velit porttitor sed imperdiet ac ullamcor-per Fusce eget tortor vel magna iaculis convallis. Aeneanecis vitae metus pellentesque tincidunt.Cum sociis natoque penatibus et magnis dis parturient montes.</p>
  <div class="dl">Free Download On</div>
  <i class="store" style="left:330px"></i>
  <i class="store" style="left:378px"></i>
  <div class="devices" role="img" aria-label="Illustration of tilted phone and tablet screens showing app interfaces"></div>
</section>

<h2 class="abs section-title display" style="top:2966px;font-size:36px">client testimonials</h2>
<div class="circle-nav" style="left:85px"><svg width="10" height="16" viewBox="0 0 10 16"><path d="M8 2L2 8l6 6" fill="none" stroke="#ccc" stroke-width="2"/></svg></div>
<div class="circle-nav" style="left:1073px"><svg width="10" height="16" viewBox="0 0 10 16"><path d="M2 2l6 6-6 6" fill="none" stroke="#ccc" stroke-width="2"/></svg></div>
<div class="quote dark">Lorem ipsum dolor sit amet, consectetur adipiscing elit. Enim, delectus atque odit esse harum! Saepe!</div>
<svg class="abs" style="left:860px;top:3261px" width="30" height="22" viewBox="0 0 30 22"><polygon points="0,0 30,0 8,22" fill="#333"/></svg>
<div class="quote blue">Lorem ipsum dolor sit amet, consectetur adipiscing elit. Enim, delectus atque odit esse harum! Saepe!</div>
<svg class="abs" style="left:460px;top:3216px;z-index:2" width="30" height="22" viewBox="0 0 30 22"><polygon points="0,0 30,0 8,22" fill="#1aa3e8"/></svg>
<div class="person">
  <div class="avatar" style="left:200px;top:3236px" role="img" aria-label="Portrait of John Doe"></div>
  <b style="left:252px;top:3236px">John Doe</b><span style="left:252px;top:3262px">Web designer</span>
  <div class="avatar" style="left:604px;top:3270px" role="img" aria-label="Portrait of Jessica Doe"></div>
  <b style="left:656px;top:3270px">Jessica Doe</b><span style="left:666px;top:3296px">Developer</span>
</div>

<footer class="abs footer">
  <div class="abs brand"><i class="brand-dot"></i>overthread</div>
  <p class="about">Overthread is a registered builder and member of the Kestrel Valley Builders Guild.</p>
  <i class="soc" style="left:100px"></i><i class="soc" style="left:136px"></i><i class="soc" style="left:172px"></i><i class="soc" style="left:208px"></i>

  <h4 style="left:356px">GET IN TOUCH</h4>
  <ul class="touch" style="left:356px;top:84px;width:220px">
    <li><i></i><span>77 Harbor Row, Lindenfield 40211</span></li>
    <li><i></i><span>(555) 014-8896</span></li>
    <li><i></i><span>hello@overthread.example</span></li>
    <li><i></i><span>(555) 014-8896</span></li>
    <li><i></i><span>Mon - Sat: 9:00 - 18:00</span></li>
  </ul>

  <h4 style="left:612px">INFORMATION</h4>
  <ul class="info" style="left:612px;top:84px">
    <li>HOME</li><li>OUR STORY</li><li>OUR PEOPLE</li><li>WHAT WE DO</li><li>CONTACT US</li>
  </ul>

  <h4 style="left:871px">NEWS LETTER</h4>
  <p class="nl">Enter your email address for our mailing list to keep your self our lastest updated.</p>
  <div class="input">Email</div>
  <div class="signup">Sign up</div>
</footer>
<div class="abs copyright">Copyright © 2007 - 2016 OVERTHREAD. All Rights Reserved</div>

</body>
</html>
```